Kel Video Games

I need a design for a campaign game, pure news no sale, it fun and modern, and also something different and do it to the other pages there, the design must convey the central idea of ​​the page. You should be able to get on the platform wordpress

Industry/Entity Type

Games

Number of Pages Required

1 page

Font styles to use
Sans Serif

```html
<!DOCTYPE html>
<html lang="en">
<head>
<meta charset="utf-8">
<title>Kel Video Games</title>
<link rel="stylesheet" href="https://fonts.googleapis.com/css2?family=Raleway:wght@500;600;700;800&family=Open+Sans:wght@400;600;700&display=swap">
<style>
:root{
  --red:#b3141c;
  --red-text:#a31920;
  --orange:#efa76a;
  --ink:#222;
  --muted:#8a8a8a;
  --line:#d9d9d9;
  --footer-top:#9b1a1d;
  --footer-bottom:#3a0b0c;
  --ad-blue:#1f78d0;
  --ad-sky:#3a9fd8;
}
*{box-sizing:border-box;margin:0;padding:0}
html,body{width:1200px;height:2769px;overflow:hidden;background:#fff}
body{font-family:"Open Sans",Arial,sans-serif;color:var(--ink);position:relative}
h1,h2,h3,h4{font-family:"Raleway",Arial,sans-serif}

/* header */
.site-header{position:absolute;left:0;top:0;width:1200px;height:100px;background:#fff}
.brand{position:absolute;left:129px;top:24px;display:flex;align-items:center;gap:10px}
.brand-mark{width:44px;height:44px;background:var(--red);border-radius:6px}
.brand-name{font-family:"Raleway",Arial,sans-serif;font-weight:800;font-size:40px;color:var(--ink);letter-spacing:-1px}
.main-nav a{position:absolute;top:39px;font-family:"Raleway",Arial,sans-serif;font-weight:600;font-size:15px;color:var(--red-text);text-decoration:none;letter-spacing:.3px}
.search-icon{position:absolute;left:996px;top:36px}

/* hero */
.hero{position:absolute;left:0;top:100px;width:1200px;height:426px;overflow:hidden}
.hero-main{position:absolute;inset:0;background:linear-gradient(120deg,#3a3a38 0%,#6a5a3c 35%,#3c3226 60%,#5a4a3a 100%)}
.hero-shade{position:absolute;inset:0;background:linear-gradient(0deg,rgba(0,0,0,.5),rgba(0,0,0,0) 60%)}
.hero-side-top{position:absolute;inset:0;background:linear-gradient(135deg,#2a2a30,#5a2a2c 60%,#3a2024);clip-path:polygon(729px 0,1200px 0,1200px 214px,690px 214px)}
.hero-side-bottom{position:absolute;inset:0;background:linear-gradient(135deg,#d41d23,#a0121a);clip-path:polygon(688px 218px,1200px 218px,1200px 426px,637px 426px)}
.hero-edge{position:absolute;inset:0;background:#e0232a;clip-path:polygon(722px 0,731px 0,639px 426px,630px 426px)}
.hero-title{position:absolute;left:129px;top:220px;font-weight:700;font-size:31px;color:#fff;letter-spacing:.3px}
.hero-text{position:absolute;left:129px;top:262px;width:390px;font-size:13px;line-height:24px;color:#eee}
.hero-dots{position:absolute;left:129px;top:318px;display:flex;gap:5px}
.hero-dots span{width:16px;height:16px;border-radius:50%;background:#fff;border:2px solid #fff}
.hero-dots span.active{background:transparent}
.side-caption{position:absolute;font-family:"Raleway",Arial,sans-serif;font-weight:700;color:#fff;font-size:24px;line-height:28px}

/* section titles */
.section-title{position:absolute;font-weight:600;text-transform:uppercase}
.section-title.red{color:var(--red-text);font-size:24px}
.section-title.dark{color:#222;font-size:18px}

/* top games */
.game-card{position:absolute;top:604px;width:220px;height:208px;border-bottom:1px solid var(--line)}
.game-card .thumb{width:220px;height:142px}
.card-title{font-family:"Open Sans",Arial,sans-serif;font-weight:400;font-size:15px;color:#222;margin-top:8px}
.card-text{font-size:12px;color:var(--muted);margin-top:4px}

/* video */
.video-block{position:absolute;left:124px;top:846px;width:614px;height:273px;border:1px solid #e6e6e6;padding:6px}
.video-thumb{width:100%;height:100%;background:linear-gradient(160deg,#8b8f8c,#3c4042 45%,#626a6c 100%);position:relative}
.video-label{position:absolute;left:0;right:0;top:64px;text-align:center;font-family:"Raleway",Arial,sans-serif;font-weight:600;color:#fff;font-size:24px}
.play{position:absolute;left:259px;top:104px}

/* upcoming */
.upcoming{position:absolute;left:766px;top:846px;width:303px;height:579px;border:1px solid #e1e1e1;background:#fff}
.upcoming-head{height:53px;background:var(--orange);color:#fff;font-family:"Raleway",Arial,sans-serif;font-weight:600;font-size:17px;padding:16px 24px}
.upcoming-item{height:115px;border-bottom:1px solid #e6e6e6;display:flex;align-items:center;padding-left:18px;gap:16px}
.upcoming-item .avatar{width:92px;height:92px;border-radius:50%;flex:none}
.upcoming-item h4{font-family:"Open Sans",Arial,sans-serif;font-weight:400;font-size:14px;color:#222}
.upcoming-item p{font-size:12px;line-height:18px;color:var(--muted);margin-top:4px;width:160px}
.view-more{position:absolute;left:0;right:0;bottom:0;height:32px;border-top:1px solid #e1e1e1;background:#f6f6f6;text-align:center;font-size:13px;color:#666;line-height:32px}

/* popular */
.popular-card{position:absolute;top:1176px;width:301px}
.popular-card .thumb{height:133px}
.read-more{font-size:12px;font-weight:700;color:var(--red-text);text-transform:uppercase;display:block}
.dash-divider{position:absolute;left:126px;width:615px;height:4px;background:repeating-linear-gradient(90deg,#cfcfcf 0 4px,transparent 4px 7px)}

/* latest news */
.news-item{position:absolute;left:129px;width:620px;height:92px}
.news-item .thumb{position:absolute;left:0;top:0;width:150px;height:92px}
.news-item .body{position:absolute;left:163px;top:4px;width:460px}
.news-item h4{font-family:"Open Sans",Arial,sans-serif;font-weight:400;font-size:14px;color:#222}
.news-item p{font-size:12px;line-height:20px;color:var(--muted);margin-top:6px}
.news-item .read-more{margin-top:6px}

/* ad slots */
.ad-slot{position:absolute;left:768px;width:301px}
.ad-slot.one{top:1442px;height:251px;background:linear-gradient(180deg,#2f8ee0,var(--ad-blue))}
.ad-slot.two{top:1717px;height:247px;background:linear-gradient(180deg,var(--ad-sky),#2a86c4)}

.dragon-bg{position:absolute;left:700px;top:1740px;width:500px;height:620px;background:radial-gradient(ellipse at 70% 40%,rgba(150,120,120,.22),rgba(255,255,255,0) 65%)}

/* blog */
.blog-arrow{position:absolute;top:2048px;width:28px;height:28px}
.blog-card{position:absolute;top:2090px;width:294px;height:279px;border:1px solid #ddd;background:#fff}
.blog-card .thumb{height:149px}
.blog-card .body{padding:14px 24px}
.blog-card h4{font-family:"Open Sans",Arial,sans-serif;font-weight:400;font-size:15px;color:#222}
.blog-card p{font-size:12px;line-height:20px;color:var(--muted);margin-top:6px}
.blog-card .read-more{margin-top:6px}

/* footer */
.site-footer{position:absolute;left:0;top:2440px;width:1200px;height:274px;background:linear-gradient(135deg,#b3262a,var(--footer-top) 40%,#5e1214 100%)}
.foot-col{position:absolute;top:76px}
.foot-col h5{font-family:"Raleway",Arial,sans-serif;font-weight:700;font-size:13px;color:#fff;text-transform:uppercase;margin-bottom:14px}
.foot-col a{display:block;font-size:12px;color:#f2dede;text-decoration:none;line-height:29px}
.foot-col .note{font-size:12px;color:#f2dede}
.email-field{margin-top:10px;width:245px;height:32px;background:#fff;font-size:11px;color:#aaa;padding:0 12px;line-height:32px}
.subscribe-btn{margin-top:12px;width:105px;height:30px;background:#c8141c;color:#fff;font-size:12px;font-weight:600;text-align:center;line-height:30px;text-transform:uppercase}
.social{display:flex;gap:12px;margin-top:6px}
.social span{width:35px;height:35px;border-radius:50%;background:#fff;display:block}
.copyright-bar{position:absolute;left:0;top:2714px;width:1200px;height:55px;background:var(--footer-bottom);text-align:center;color:#a98a8a;font-size:12px;line-height:55px}
</style>
</head>
<body>

<header class="site-header">
  <div class="brand"><span class="brand-mark"></span><span class="brand-name">KELGAMES</span></div>
  <nav class="main-nav">
    <a style="left:462px">GAMES</a>
    <a style="left:548px">LATEST</a>
    <a style="left:637px">NEWS</a>
    <a style="left:716px">REVIEWS</a>
    <a style="left:816px">VIDEOS</a>
    <a style="left:905px">FORUMS</a>
  </nav>
  <svg class="search-icon" width="22" height="22" viewBox="0 0 22 22"><circle cx="9" cy="9" r="6" fill="none" stroke="#a31920" stroke-width="3"/><line x1="13.5" y1="13.5" x2="19" y2="19" stroke="#a31920" stroke-width="3" stroke-linecap="round"/></svg>
</header>

<section class="hero">
  <div class="hero-main" role="img" aria-label="Sci-fi battle scene with a spaceship over a ruined city"></div>
  <div class="hero-shade"></div>
  <div class="hero-side-top" role="img" aria-label="Armoured war robot artwork"></div>
  <div class="hero-side-bottom" role="img" aria-label="Red tinted game artwork"></div>
  <div class="hero-edge"></div>
  <h1 class="hero-title">DONEC DICTUM LECTUS NON</h1>
  <p class="hero-text">Pellentesque habitant morbi tristique senectus et netus et malesuada fames ac turpis egestas Cras.</p>
  <div class="hero-dots"><span class="active"></span><span></span><span></span><span></span></div>
  <div class="side-caption" style="left:724px;top:144px">CUM SOCIS NATOQUE<br>PELLENTESQUE FAUCIBUS</div>
  <div class="side-caption" style="left:718px;top:354px">MORBI PORTA LIBE<br>ULLAMCORPER NONU</div>
</section>

<h2 class="section-title red" style="left:133px;top:560px">Latest Top Games</h2>
<article class="game-card" style="left:131px"><div class="thumb" role="img" aria-label="Volcanic landscape with fiery sky" style="background:linear-gradient(160deg,#5a2a14,#c2501c 50%,#2a1a12)"></div><h3 class="card-title">Praesent elementum</h3><p class="card-text">elit at tellus nec ultricies sit amet</p></article>
<article class="game-card" style="left:371px"><div class="thumb" role="img" aria-label="Armoured mech warrior in blue light" style="background:linear-gradient(160deg,#2a3a6a,#5a6a9a 50%,#1a2240)"></div><h3 class="card-title">Cum sociis natoque</h3><p class="card-text">elit at tellus nec ultricies sit amet</p></article>
<article class="game-card" style="left:609px"><div class="thumb" role="img" aria-label="Fantasy city under a purple sky" style="background:linear-gradient(160deg,#3a6aa0,#7a4a9a 50%,#2a2a4a)"></div><h3 class="card-title">Quisque dignissim congue</h3><p class="card-text">elit at tellus nec ultricies sit amet</p></article>
<article class="game-card" style="left:849px"><div class="thumb" role="img" aria-label="Dragon over a rocky coast" style="background:linear-gradient(160deg,#8ab0c0,#c07a4a 50%,#5a6a70)"></div><h3 class="card-title">Cum sociis natoque pe</h3><p class="card-text">elit at tellus nec ultricies sit amet</p></article>

<div class="video-block">
  <div class="video-thumb" role="img" aria-label="Giant robot in a smoky battlefield">
    <div class="video-label">NEWLEY LAUNCHED</div>
    <svg class="play" width="84" height="84" viewBox="0 0 84 84"><circle cx="42" cy="42" r="39" fill="none" stroke="#fff" stroke-width="3"/><polygon points="34,26 60,42 34,58" fill="#fff"/></svg>
  </div>
</div>

<aside class="upcoming">
  <div class="upcoming-head">UPCOMING GAMES</div>
  <div class="upcoming-item"><div class="avatar" role="img" aria-label="Dark game artwork" style="background:radial-gradient(circle,#8a8a8a,#1a1a1a)"></div><div><h4>GAME TITTLE</h4><p>Praesent elementum elit at tellus nec ultricies sit amet porttitor mattis enim</p></div></div>
  <div class="upcoming-item"><div class="avatar" role="img" aria-label="Blue glowing game artwork" style="background:radial-gradient(circle,#6a8ae0,#101a5a)"></div><div><h4>GAME TITTLE</h4><p>Praesent elementum elit at tellus nec ultricies sit amet porttitor mattis enim</p></div></div>
  <div class="upcoming-item"><div class="avatar" role="img" aria-label="Shadowy warrior artwork" style="background:radial-gradient(circle,#5a6a70,#1a2226)"></div><div><h4>GAME TITTLE</h4><p>Praesent elementum elit at tellus nec ultricies sit amet porttitor mattis enim</p></div></div>
  <div class="upcoming-item"><div class="avatar" role="img" aria-label="Warm toned fantasy artwork" style="background:radial-gradient(circle,#b08a6a,#3a2a22)"></div><div><h4>GAME TITTLE</h4><p>Praesent elementum elit at tellus nec ultricies sit amet porttitor mattis enim</p></div></div>
  <div class="view-more">VIEW MORE</div>
</aside>

<h2 class="section-title dark" style="left:126px;top:1138px">Popular News</h2>
<article class="popular-card" style="left:126px"><div class="thumb" role="img" aria-label="Dragon breathing fire in golden haze" style="background:linear-gradient(160deg,#e0a050,#8a4a1a 50%,#3a2010)"></div><h3 class="card-title">Cum socis natoque</h3><p class="card-text" style="line-height:18px">Donec dictum lectus non odio Cras a ante vitae enim iaculis aliquam Mauris nunc</p><span class="read-more" style="margin-top:4px">Read More</span></article>
<article class="popular-card" style="left:436px"><div class="thumb" role="img" aria-label="Futuristic street at sunset" style="background:linear-gradient(160deg,#e0b070,#b05a3a 50%,#4a3a4a)"></div><h3 class="card-title">Fusce ultricies orci ac feugiat</h3><p class="card-text" style="line-height:18px">Donec dictum lectus non odio Cras a ante vitae enim iaculis aliquam Mauris nunc</p><span class="read-more" style="margin-top:4px">Read More</span></article>

<div class="dash-divider" style="top:1425px"></div>

<div class="dragon-bg" role="img" aria-label="Faint dragon artwork in the background"></div>

<h2 class="section-title dark" style="left:129px;top:1452px">Latest News</h2>
<article class="news-item" style="top:1495px"><div class="thumb" role="img" aria-label="Green valley with waterfalls" style="background:linear-gradient(160deg,#a0c0a0,#4a7a4a 60%,#2a4a3a)"></div><div class="body"><h4>Morbi porta libero id ullamcorper nonummy</h4><p>Etiam est nunc venenatis in tristique eu imperdiet ac nisl Cum sociis natoque penatibus et magnis dis parturient montes</p><span class="read-more">Read More</span></div></article>
<article class="news-item" style="top:1622px"><div class="thumb" role="img" aria-label="Blue magical cave scene" style="background:linear-gradient(160deg,#3a4a7a,#1a1a3a 60%,#5a6aa0)"></div><div class="body"><h4>Nullam enim leo egestas</h4><p>Etiam est nunc venenatis in tristique eu imperdiet ac nisl Cum sociis natoque penatibus et magnis dis parturient montes</p><span class="read-more">Read More</span></div></article>
<article class="news-item" style="top:1749px"><div class="thumb" role="img" aria-label="Red sky over dark water" style="background:linear-gradient(160deg,#c04a2a,#3a3a5a 60%,#1a2a4a)"></div><div class="body"><h4>Nullam enim leo egestas</h4><p>Etiam est nunc venenatis in tristique eu imperdiet ac nisl Cum sociis natoque penatibus et magnis dis parturient montes</p><span class="read-more">Read More</span></div></article>
<article class="news-item" style="top:1876px"><div class="thumb" role="img" aria-label="Glowing red fantasy tower" style="background:linear-gradient(160deg,#2a3a4a,#a03a2a 55%,#1a1a22)"></div><div class="body"><h4>Nullam enim leo egestas</h4><p>Etiam est nunc venenatis in tristique eu imperdiet ac nisl Cum sociis natoque penatibus et magnis dis parturient montes</p><span class="read-more">Read More</span></div></article>

<div class="ad-slot one" role="img" aria-label="Sidebar advertisement banner"></div>
<div class="ad-slot two" role="img" aria-label="Sidebar advertisement banner"></div>

<div class="dash-divider" style="left:129px;top:2014px;width:940px"></div>

<h2 class="section-title red" style="left:129px;top:2044px">From the Blog</h2>
<svg class="blog-arrow" style="left:996px" viewBox="0 0 28 28"><circle cx="14" cy="14" r="14" fill="#222"/><polyline points="16,8 10,14 16,20" fill="none" stroke="#fff" stroke-width="2.5"/></svg>
<svg class="blog-arrow" style="left:1030px" viewBox="0 0 28 28"><circle cx="14" cy="14" r="14" fill="#222"/><polyline points="12,8 18,14 12,20" fill="none" stroke="#fff" stroke-width="2.5"/></svg>

<article class="blog-card" style="left:129px"><div class="thumb" role="img" aria-label="Candy land game background" style="background:linear-gradient(180deg,#e0c0f0,#c090e0 50%,#8a5ab0)"></div><div class="body"><h4>Nullam enim leo egestas</h4><p>Etiam est nunc venenatis in tristique eu imperdiet ac nisl Cum sociis natoque</p><span class="read-more">Read More</span></div></article>
<article class="blog-card" style="left:449px"><div class="thumb" role="img" aria-label="Alien planet game background" style="background:linear-gradient(180deg,#f0a070,#b05a8a 50%,#6a3a7a)"></div><div class="body"><h4>Nullam enim leo egestas</h4><p>Etiam est nunc venenatis in tristique eu imperdiet ac nisl Cum sociis natoque</p><span class="read-more">Read More</span></div></article>
<article class="blog-card" style="left:768px"><div class="thumb" role="img" aria-label="Dark cave game background" style="background:linear-gradient(180deg,#4a2a2a,#7a4a40 50%,#2a1a1a)"></div><div class="body"><h4>Nullam enim leo egestas</h4><p>Etiam est nunc venenatis in tristique eu imperdiet ac nisl Cum sociis natoque</p><span class="read-more">Read More</span></div></article>

<footer class="site-footer">
  <div class="foot-col" style="left:131px"><h5>Company</h5><a>Home</a><a>About Us</a><a>Upcoming Games</a><a>Download Now</a></div>
  <div class="foot-col" style="left:290px"><h5>Resources</h5><a>Help</a><a>Latest News</a><a>Articles</a><a>Term of Use</a></div>
  <div class="foot-col" style="left:449px"><h5>Support</h5><a>FAQ</a><a>Support</a><a>Our Blogs</a><a>Contcat Us</a></div>
  <div class="foot-col" style="left:604px"><h5>Email Subscribe</h5><p class="note">Please sign up here for latest news</p><div class="email-field">Email address</div><div class="subscribe-btn">Subscribe</div></div>
  <div class="foot-col" style="left:897px"><h5>Follow Us</h5><div class="social"><span></span><span></span><span></span><span></span></div></div>
</footer>
<div class="copyright-bar">© 2016 Company Name. All right reserved</div>

</body>
</html>
```